Medical Company in need of a Modern Flyer design for new Wound Care clinic.

Tri-Fold modern flyer design for our Woundcare company. Logo and description of services can be found on our website; https://www.birchline-woundcare.com/

```html
<!DOCTYPE html>
<html lang="en">
<head>
<meta charset="utf-8">
<title>Birchline Wound Care – Tri-Fold Brochure</title>
<link rel="stylesheet" href="https://fonts.googleapis.com/css2?family=Montserrat:wght@400;700;800&family=Poppins:wght@300;400&display=swap">
<style>
  :root {
    --backdrop: #3d3d3d;
    --paper: #ffffff;
    --ink: #141414;
    --ink-soft: #2a2a2a;
    --gold-deep: #c98a1c;
    --gold-mid: #e9b446;
    --gold-light: #f8dc8a;
  }
  html, body {
    margin: 0;
    padding: 0;
    width: 873px;
    height: 1200px;
    overflow: hidden;
    background: var(--backdrop);
  }
  .stage {
    position: absolute;
    left: 0;
    top: 0;
    width: 960px;
    height: 1320px;
    transform: scale(0.909375);
    transform-origin: 0 0;
  }
  .sheet {
    position: absolute;
    left: 65px;
    width: 830px;
    height: 588px;
    background: var(--paper);
    overflow: hidden;
  }
  .sheet--outside { top: 48px; }
  .sheet--inside { top: 684px; height: 587px; }
  .sheet__art {
    position: absolute;
    inset: 0;
    width: 100%;
    height: 100%;
  }
  .heading {
    position: absolute;
    margin: 0;
    font-family: "Montserrat", Arial, sans-serif;
    font-weight: 800;
    color: var(--ink);
    letter-spacing: -0.2px;
  }
  .body-copy {
    position: absolute;
    margin: 0;
    font-family: "Poppins", Arial, sans-serif;
    font-weight: 300;
    font-size: 11.4px;
    line-height: 14.2px;
    color: var(--ink-soft);
  }

  /* Outside panels */
  .contact {
    position: absolute;
    left: 281px;
    top: 312px;
    width: 170px;
    text-align: center;
    font-family: "Poppins", Arial, sans-serif;
    color: var(--ink);
  }
  .contact__title {
    margin: 0 0 8px;
    font-family: "Montserrat", Arial, sans-serif;
    font-weight: 800;
    font-size: 21px;
  }
  .contact__icon { display: block; margin: 0 auto; }
  .contact__phone {
    margin: 3px 0 8px;
    font-weight: 400;
    font-size: 12.5px;
    font-family: "Montserrat", Arial, sans-serif;
    font-weight: 700;
  }
  .contact__address {
    margin: 5px 0 0;
    font-size: 12.5px;
    line-height: 15px;
    font-weight: 400;
  }
  .brand {
    position: absolute;
    left: 555px;
    top: 62px;
    width: 275px;
    text-align: center;
  }
  .brand__mark {
    display: block;
    width: 26px;
    height: 26px;
    margin: 0 auto 14px;
    background: var(--gold-mid);
  }
  .brand__name {
    margin: 0;
    font-family: "Montserrat", Arial, sans-serif;
    font-weight: 400;
    font-size: 15px;
    letter-spacing: 2.6px;
    color: var(--ink);
  }

  /* Inside panels */
  .about__title { left: 16px; top: 26px; font-size: 20px; }
  .about__text { left: 16px; top: 57px; width: 250px; }
  .tagline {
    right: 569px;
    top: 286px;
    font-size: 29px;
    line-height: 29.5px;
    text-align: right;
  }
  .services__title { left: 300px; top: 20px; width: 230px; text-align: center; font-size: 24px; }
  .services__list {
    position: absolute;
    left: 288px;
    top: 68px;
    width: 255px;
    margin: 0;
    padding: 0;
    list-style: none;
    font-family: "Poppins", Arial, sans-serif;
    font-weight: 400;
    font-size: 11.6px;
    line-height: 14px;
    color: var(--ink);
  }
  .services__item {
    position: relative;
    padding-left: 34px;
    margin-bottom: 14.5px;
  }
  .services__bullet {
    position: absolute;
    left: 0;
    top: -1px;
  }
  .hbo__title {
    right: 17px;
    top: 210px;
    font-size: 23.5px;
    line-height: 29.5px;
    text-align: right;
  }
  .hbo__text {
    right: 17px;
    top: 310px;
    width: 250px;
    text-align: right;
  }
</style>
</head>
<body>
<div class="stage">

  <!-- Outside of the brochure -->
  <section class="sheet sheet--outside">
    <svg class="sheet__art" viewBox="0 0 830 588" preserveAspectRatio="none" aria-hidden="false">
      <defs>
        <linearGradient id="goldOut" x1="0" y1="0" x2="1" y2="1">
          <stop offset="0" stop-color="#c98a1c"/>
          <stop offset="0.5" stop-color="#f8dc8a"/>
          <stop offset="1" stop-color="#e0a332"/>
        </linearGradient>
        <linearGradient id="goldContact" x1="0" y1="0" x2="1" y2="1">
          <stop offset="0" stop-color="#e6a72c"/>
          <stop offset="0.6" stop-color="#f7cf63"/>
          <stop offset="1" stop-color="#fbe49b"/>
        </linearGradient>
        <linearGradient id="waitingRoom" x1="0" y1="0" x2="1" y2="0">
          <stop offset="0" stop-color="#a99b86"/>
          <stop offset="0.6" stop-color="#c8a568"/>
          <stop offset="1" stop-color="#dca848"/>
        </linearGradient>
        <linearGradient id="lab" x1="0" y1="0" x2="1" y2="1">
          <stop offset="0" stop-color="#dfe6ec"/>
          <stop offset="1" stop-color="#9fb8cf"/>
        </linearGradient>
        <linearGradient id="glove" x1="0" y1="0" x2="1" y2="1">
          <stop offset="0" stop-color="#d2d8dd"/>
          <stop offset="0.5" stop-color="#5f9fc0"/>
          <stop offset="1" stop-color="#e7ebee"/>
        </linearGradient>
      </defs>
      <polygon points="185,0 555,0 555,430 277,112" fill="url(#lab)" role="img" aria-label="Photo: clinician working at a computer in a laboratory"/>
      <polygon points="555,330 830,150 830,588 730,588 555,400" fill="url(#glove)" role="img" aria-label="Photo: gloved hand with floating teal medical icons"/>
      <polygon points="0,0 185,0 277,112 277,588 0,588" fill="url(#waitingRoom)" role="img" aria-label="Photo: patients seated in a clinic waiting room with a masked doctor"/>
      <polygon points="300,0 362,0 830,535 830,588 800,588" fill="url(#goldOut)"/>
      <polygon points="830,128 830,178 604,392 586,372" fill="url(#goldOut)"/>
      <polygon points="277,112 540,398 277,588" fill="url(#goldContact)"/>
      <polygon points="540,398 558,414 312,588 285,588" fill="#ffffff"/>
      <polygon points="558,414 676,588 312,588" fill="url(#goldOut)"/>
    </svg>

    <div class="contact">
      <h2 class="contact__title">CONTACT US</h2>
      <svg class="contact__icon" width="14" height="14" viewBox="0 0 24 24" aria-hidden="true">
        <path d="M6.6 10.8a15 15 0 0 0 6.6 6.6l2.2-2.2a1 1 0 0 1 1-.25 11.4 11.4 0 0 0 3.6.57 1 1 0 0 1 1 1V20a1 1 0 0 1-1 1A17 17 0 0 1 3 4a1 1 0 0 1 1-1h3.5a1 1 0 0 1 1 1c0 1.25.2 2.45.57 3.57a1 1 0 0 1-.25 1z" fill="#141414"/>
      </svg>
      <p class="contact__phone">972-555-0148</p>
      <svg class="contact__icon" width="17" height="12" viewBox="0 0 17 12" aria-hidden="true">
        <rect x="0.5" y="0.5" width="16" height="11" fill="#141414"/>
        <polyline points="0.5,0.5 8.5,7 16.5,0.5" fill="none" stroke="#f7cf63" stroke-width="1.2"/>
      </svg>
      <p class="contact__address">2810 Harlow Ave Ste 200<br>Suite 4417 Dallas,<br>TX 75204</p>
    </div>

    <div class="brand">
      <span class="brand__mark"></span>
      <p class="brand__name">BIRCHLINE WOUNDCARE</p>
    </div>
  </section>

  <!-- Inside of the brochure -->
  <section class="sheet sheet--inside">
    <svg class="sheet__art" viewBox="0 0 830 587" preserveAspectRatio="none">
      <defs>
        <linearGradient id="goldIn" x1="0" y1="0" x2="1" y2="1">
          <stop offset="0" stop-color="#c98a1c"/>
          <stop offset="0.5" stop-color="#f8dc8a"/>
          <stop offset="1" stop-color="#d99c2a"/>
        </linearGradient>
        <linearGradient id="silver" x1="1" y1="0" x2="0" y2="1">
          <stop offset="0" stop-color="#5c5c5c"/>
          <stop offset="1" stop-color="#d6d6d6"/>
        </linearGradient>
        <linearGradient id="softGrey" x1="0" y1="0" x2="1" y2="1">
          <stop offset="0" stop-color="#bdbdbd"/>
          <stop offset="1" stop-color="#f4f4f4"/>
        </linearGradient>
        <linearGradient id="doctor" x1="0" y1="0" x2="0" y2="1">
          <stop offset="0" stop-color="#cfd9df"/>
          <stop offset="1" stop-color="#5b86bf"/>
        </linearGradient>
        <linearGradient id="hands" x1="0" y1="0" x2="1" y2="1">
          <stop offset="0" stop-color="#f2e6cf"/>
          <stop offset="0.6" stop-color="#f0cfa6"/>
          <stop offset="1" stop-color="#e2c69a"/>
        </linearGradient>
        <linearGradient id="knee" x1="0" y1="0" x2="1" y2="0">
          <stop offset="0" stop-color="#e0b79c"/>
          <stop offset="1" stop-color="#f1f1f1"/>
        </linearGradient>
      </defs>
      <polygon points="0,265 70,265 265,587 0,587" fill="url(#doctor)" role="img" aria-label="Photo: smiling surgeon in blue scrubs"/>
      <polygon points="277,258 400,258 676,587 277,587" fill="url(#hands)" role="img" aria-label="Photo: caregiver's hands tending a patient's bandaged hand"/>
      <polygon points="553,0 830,0 830,12 650,228 553,228" fill="url(#knee)" role="img" aria-label="Photo: clinician examining a patient's knee"/>
      <polygon points="822,0 830,0 830,26 680,210 662,210" fill="url(#goldIn)"/>
      <polygon points="276,170 276,194 94,354 76,342" fill="url(#silver)"/>
      <polygon points="555,440 700,587 555,587" fill="url(#softGrey)"/>
      <polygon points="555,398 572,404 752,587 724,587 555,426" fill="url(#goldIn)"/>
    </svg>

    <h2 class="heading about__title">ABOUT US</h2>
    <p class="body-copy about__text">At Birchline Wound Care, we specialize in managing outpatient wound care facilities throughout the Dallas/Fort Worth area. Partnering with hospitals and local rehabilitation units, we deliver the most advanced wound care treatments. Our commitment to quality care resonates through our collaboration with small practice family providers, ensuring personalized, effective treatment plans.</p>

    <h2 class="heading tagline">YOUR<br>HEALTH<br>IS OUR<br>PRIORITY</h2>

    <h2 class="heading services__title">OUR SERVICES</h2>
    <ul class="services__list">
      <li class="services__item"><svg class="services__bullet" width="18" height="18" viewBox="0 0 18 18" aria-hidden="true"><path d="M6 0h6v6h6v6h-6v6H6v-6H0V6h6z" fill="#efc056"/></svg>Hyperbaric Oxygen Therapy (HBO): A Cornerstone of Advanced Wound Care</li>
      <li class="services__item"><svg class="services__bullet" width="18" height="18" viewBox="0 0 18 18" aria-hidden="true"><path d="M6 0h6v6h6v6h-6v6H6v-6H0V6h6z" fill="#efc056"/></svg>Debridement</li>
      <li class="services__item"><svg class="services__bullet" width="18" height="18" viewBox="0 0 18 18" aria-hidden="true"><path d="M6 0h6v6h6v6h-6v6H6v-6H0V6h6z" fill="#efc056"/></svg>Advanced Wound Dressings</li>
      <li class="services__item"><svg class="services__bullet" width="18" height="18" viewBox="0 0 18 18" aria-hidden="true"><path d="M6 0h6v6h6v6h-6v6H6v-6H0V6h6z" fill="#efc056"/></svg>Bio-engineered Skin Substitutes</li>
      <li class="services__item"><svg class="services__bullet" width="18" height="18" viewBox="0 0 18 18" aria-hidden="true"><path d="M6 0h6v6h6v6h-6v6H6v-6H0V6h6z" fill="#efc056"/></svg>Compression Therapy and Edema Management</li>
    </ul>

    <h2 class="heading hbo__title">HYPERBARIC<br>OXYGEN<br>THERAPY</h2>
    <p class="body-copy hbo__text">Hyperbaric Oxygen Therapy (HBO) is not just a treatment; it's a pivotal part of our comprehensive approach to wound healing at Birchline Wound Care. By delivering pure oxygen in a pressurized chamber, HBO therapy significantly increases the amount of oxygen in the blood, fostering an environment that accelerates the repair and regeneration of wounded tissues.</p>
  </section>

</div>
</body>
</html>
```